vorp business card design

vorp is an incubator within TRW Mediaworks focused on unlocking the potential in underserved niche micro-verticals on the web. our mission is to rapidly develop and foster emerging micro-verticals bc they are ripe for growth - building interesting and trusted content experiences with unqiue, useful and cutting-edge delivery methods.please do all copy (except for TRW Mediaworks, which must look as typed here and in logo) in all lowercase. Also please use spaces between phone # extensions not dashes or periods. I have attached all variations of the logo.
Industry/Entity Type
Business
Contact Information for Business Card
dale fenwright, ceo www.vorp.example 218 9th avenue 3rd floor oakland ca 94610 415 602 0002m 510 985 7966d dale.fenwright@vorp.example
Look and feel

```html
<!DOCTYPE html>
<html lang="en">
<head>
<meta charset="utf-8">
<title>vorp business card</title>
<link rel="stylesheet" href="https://fonts.googleapis.com/css2?family=Arimo:wght@400;700&display=swap">
<style>
  :root {
    --backdrop: #2a2a2c;
    --card-black: #1c1c1d;
    --card-white: #ffffff;
    --teal: #1a9497;
    --ink-dark: #2b2b2b;
    --text-grey: #4a4a4a;
    --white: #ffffff;
  }
  * { margin: 0; padding: 0; box-sizing: border-box; }
  html, body { width: 1200px; height: 750px; overflow: hidden; }
  body {
    background: var(--backdrop);
    font-family: "Arimo", Arial, sans-serif;
    position: relative;
  }
  .card {
    position: absolute;
    top: 225px;
    width: 525px;
    height: 300px;
    overflow: hidden;
    box-shadow: 0 10px 30px rgba(0,0,0,0.5);
  }
  .card--front { left: 50px; background: var(--card-black); color: var(--white); }
  .card--back { left: 625px; background: var(--card-white); color: var(--text-grey); }

  .brand { display: flex; align-items: center; gap: 8px; }
  .brand__name { font-weight: 700; font-size: 64px; line-height: 1; letter-spacing: -1px; }
  .brand__dot { width: 16px; height: 16px; border-radius: 50%; background: currentColor; margin-top: -30px; }
  .brand__tagline { font-size: 13px; margin-top: 4px; }

  .card--front .lockup {
    position: absolute; left: 0; right: 0; top: 92px;
    display: flex; flex-direction: column; align-items: center;
  }
  .card--front .brand__name { color: var(--white); }
  .card--front .brand__dot { background: var(--white); }
  .card--front .web {
    position: absolute; left: 0; right: 0; top: 232px;
    text-align: center; font-size: 11px; letter-spacing: 5px;
  }

  .card--back .sweep { position: absolute; inset: 0; }
  .card--back .person {
    position: absolute; right: 28px; top: 24px; text-align: right; color: var(--white);
  }
  .person__name { font-weight: 700; font-size: 19px; }
  .person__role { font-size: 12px; margin-top: 3px; }

  .card--back .lockup { position: absolute; left: 40px; top: 120px; }
  .card--back .brand__name { color: var(--ink-dark); }
  .card--back .brand__dot { background: var(--teal); }
  .card--back .brand__tagline { color: var(--ink-dark); font-size: 12px; margin-left: 4px; }

  .address {
    position: absolute; right: 30px; top: 132px;
    text-align: right; font-size: 13px; line-height: 1.5;
  }
  .contacts {
    position: absolute; left: 44px; top: 208px;
    list-style: none; font-size: 13px; line-height: 1.45;
  }
  .contacts li { display: flex; align-items: center; gap: 8px; }
  .contacts svg { width: 12px; height: 12px; fill: var(--teal); flex: none; }
</style>
</head>
<body>

<section class="card card--front" aria-label="card front">
  <div class="lockup">
    <div class="brand">
      <span class="brand__name">vorp</span>
      <span class="brand__dot"></span>
    </div>
    <div class="brand__tagline">an TRW Mediaworks incubator</div>
  </div>
  <div class="web">www.vorp.example</div>
</section>

<section class="card card--back" aria-label="card back">
  <svg class="sweep" viewBox="0 0 525 300" preserveAspectRatio="none">
    <path d="M0 0 H525 V108 C420 60 240 40 0 96 Z" fill="var(--teal)"/>
    <path d="M150 68 C300 40 440 58 525 112" fill="none" stroke="var(--ink-dark)" stroke-width="5"/>
  </svg>

  <div class="person">
    <div class="person__name">dale fenwright</div>
    <div class="person__role">ceo</div>
  </div>

  <div class="lockup">
    <div class="brand">
      <span class="brand__name">vorp</span>
      <span class="brand__dot"></span>
    </div>
    <div class="brand__tagline">an TRW Mediaworks incubator</div>
  </div>

  <div class="address">
    218 9th avenue<br>3rd floor<br>oakland ca 94610
  </div>

  <ul class="contacts">
    <li>
      <svg viewBox="0 0 12 12"><path d="M2 4 C2 2 4 1 6 1 C8 1 10 2 10 4 L8 5 L7 4 H5 L4 5 Z M3 6 H9 L10 11 H2 Z"/></svg>
      415 738 1194
    </li>
    <li>
      <svg viewBox="0 0 12 12"><path d="M3 0 H9 V12 H3 Z M4 1.5 V9.5 H8 V1.5 Z" fill-rule="evenodd"/></svg>
      510 247 3318
    </li>
    <li>
      <svg viewBox="0 0 12 12"><path d="M0 2 H12 V10 H0 Z M1 3 L6 7 L11 3 Z" fill-rule="evenodd"/></svg>
      dale.fenwright@vorp.example
    </li>
    <li>
      <svg viewBox="0 0 12 12"><circle cx="6" cy="6" r="6"/></svg>
      www.vorp.example
    </li>
  </ul>
</section>

</body>
</html>
```